Create modern and sleek business card for luxury real estate company

We're a "boutique" real estate office looking for a design that gets across a highly modern luxury brand. Blacks and whites are probably the best colors unless we try a silver foil for the logo. I've attached a version of our current logo here. I'd like to swap out the current font on there with Gotham Light Regular.

I'm looking to have one side of the card have the logo with the space for our agents info on the other side.

Target Market(s)

Young professionals in a "luxury" headspace

Industry/Entity Type

Real estate

Contact Information for Business Card

A place for agent name, cell number, website. The slogan "Simply Rethinking Real Estate".

Font styles to use
Other font styles liked:
• Gotham Regular

Colors

Designer to choose only greyscale colors for use in the design.

Requirements
Must have
• Matte black as the background color. Clean lines and use of contrast. A specific design aspect that will use silver foil.
Nice to have
• Up in the air on integrating a QR code
Should not have
• Any houses or other real estate related design (ex: a clip art house)

```html
<!DOCTYPE html>
<html lang="en">
<head>
<meta charset="utf-8">
<title>Ardent Realty – Business Card</title>
<link href="https://fonts.googleapis.com/css2?family=Montserrat:wght@300;400;500&display=swap" rel="stylesheet">
<style>
  :root {
    --backdrop: #646464;
    --card-black: #222222;
    --foil-silver: #dcdcdc;
    --ink-soft: #c4c4c4;
  }
  * { margin: 0; padding: 0; box-sizing: border-box; }
  html, body {
    width: 1200px; height: 840px; overflow: hidden;
    background: var(--backdrop);
    font-family: "Montserrat", sans-serif;
  }
  .canvas { position: relative; width: 1200px; height: 840px; }
  .card {
    position: absolute; top: 288px; width: 476px; height: 263px;
    background: var(--card-black); overflow: hidden; color: var(--foil-silver);
  }
  .card--front { left: 100px; }
  .card--back { left: 621px; }
  .abs { position: absolute; }

  .brand-name {
    font-weight: 300; text-transform: uppercase; letter-spacing: 0.06em;
    color: var(--foil-silver); line-height: 1; white-space: nowrap;
  }
  .card--front .brand-circle { left: 40px; top: 36px; width: 62px; height: 62px; }
  .card--front .brand-name { left: 117px; font-size: 24px; }
  .card--front .brand-name--top { top: 39px; }
  .card--front .brand-rule { left: 110px; top: 67px; width: 154px; height: 1px; background: var(--foil-silver); }
  .card--front .brand-name--bottom { top: 74px; }

  .corner-ring { left: 362px; top: -20px; width: 144px; height: 144px; }

  .agent-dot { left: 110px; top: 153px; width: 7px; height: 7px; border-radius: 50%; background: var(--foil-silver); }
  .agent-name { left: 127px; top: 145px; font-size: 16px; font-weight: 500; letter-spacing: 0.01em; }
  .agent-title { left: 127px; top: 172px; font-size: 11.5px; font-weight: 400; color: var(--ink-soft); letter-spacing: 0.02em; }

  .contact { top: 214px; font-size: 11px; font-weight: 300; color: var(--ink-soft); display: flex; align-items: center; gap: 7px; }
  .contact--phone { left: 107px; }
  .contact--web { left: 226px; }
  .contact svg { width: 11px; height: 11px; }
  .contact strong { font-weight: 500; color: var(--foil-silver); }

  .card--back .brand-circle { left: 81px; top: 86px; width: 90px; height: 90px; }
  .card--back .brand-name { left: 190px; font-size: 33px; }
  .card--back .brand-name--top { top: 89px; }
  .card--back .brand-rule { left: 179px; top: 131px; width: 219px; height: 1.5px; background: var(--foil-silver); }
  .card--back .brand-name--bottom { top: 139px; }
</style>
</head>
<body>
<main class="canvas">
  <section class="card card--front" aria-label="Business card, agent side">
    <svg class="abs corner-ring" viewBox="0 0 144 144" aria-hidden="true">
      <circle cx="72" cy="72" r="70" fill="none" stroke="var(--foil-silver)" stroke-width="2"/>
    </svg>
    <svg class="abs brand-circle" viewBox="0 0 62 62" aria-hidden="true">
      <circle cx="31" cy="31" r="30" fill="none" stroke="var(--foil-silver)" stroke-width="1.5"/>
    </svg>
    <div class="abs brand-name brand-name--top">Ardent</div>
    <div class="abs brand-rule"></div>
    <div class="abs brand-name brand-name--bottom">Realty</div>

    <span class="abs agent-dot"></span>
    <p class="abs agent-name">Marco Ellison</p>
    <p class="abs agent-title">Co Founder</p>

    <p class="abs contact contact--phone">
      <svg viewBox="0 0 24 24" aria-hidden="true"><path fill="var(--ink-soft)" d="M6.6 10.8a15.1 15.1 0 0 0 6.6 6.6l2.2-2.2c.3-.3.7-.4 1-.2 1.1.4 2.3.6 3.6.6.6 0 1 .4 1 1V20c0 .6-.4 1-1 1A17 17 0 0 1 3 4c0-.6.4-1 1-1h3.5c.6 0 1 .4 1 1 0 1.3.2 2.5.6 3.6.1.3 0 .7-.2 1z"/></svg>
      <span>(123) 123 12 12</span>
    </p>
    <p class="abs contact contact--web">
      <svg viewBox="0 0 24 24" aria-hidden="true" fill="none" stroke="var(--ink-soft)" stroke-width="1.6"><circle cx="12" cy="12" r="10"/><path d="M2 12h20M12 2c3 3 3 17 0 20M12 2c-3 3-3 17 0 20"/></svg>
      <span>www.<strong>website</strong>.com</span>
    </p>
  </section>

  <section class="card card--back" aria-label="Business card, brand side">
    <svg class="abs brand-circle" viewBox="0 0 90 90" aria-hidden="true">
      <circle cx="45" cy="45" r="43.5" fill="none" stroke="var(--foil-silver)" stroke-width="2"/>
    </svg>
    <div class="abs brand-name brand-name--top">Ardent</div>
    <div class="abs brand-rule"></div>
    <div class="abs brand-name brand-name--bottom">Realty</div>
  </section>
</main>
</body>
</html>
```